Veltiwell- Comprehensive quality healthcare delivered at your door.

I am looking for brochures to help promote my business. My business name is Veltiwel (see attachment and logo). This is a new health delivery system designed to provide high quality care to elderly in their communities or at home.

See attachements. The logo is already designed.

As far as services provided (see attachment)

Target Market(s)

Elderly patients

Industry/Entity Type

Business

Font styles to use
Serif

Colors

Designer to choose colors to be used in the design.

```html
<!DOCTYPE html>
<html lang="en">
<head>
<meta charset="utf-8">
<title>Veltiwel Tri-fold Brochure</title>
<link rel="stylesheet" href="https://fonts.googleapis.com/css2?family=Mulish:wght@400;600;700;800&display=swap">
<style>
  :root {
    --page-bg: #fdf1cf;
    --paper: #ffffff;
    --green-pale: #dfe9c1;
    --green-light: #c5d48f;
    --green-mid: #a1b560;
    --green-deep: #7d913a;
    --green-ink: #5a6a2a;
    --text-dark: #1f2a14;
    --text-body: #3b3b33;
    --card: #f3f3e6;
    --photo-a: #9cb17a;
    --photo-b: #d8c6a8;
  }
  * { box-sizing: border-box; margin: 0; padding: 0; }
  html, body { width: 1200px; height: 900px; overflow: hidden; }
  body {
    background: var(--page-bg);
    font-family: "Mulish", "Helvetica Neue", Arial, sans-serif;
    color: var(--text-body);
    position: relative;
  }
  .brochure {
    position: absolute; left: 140px; top: 52px; width: 920px; height: 713px;
    background: var(--paper);
    box-shadow: 3px 4px 6px rgba(0,0,0,.25);
  }
  .abs { position: absolute; }

  /* Left panel */
  .band {
    position: absolute; height: 38px; display: flex; align-items: center;
    font-size: 16px; letter-spacing: .2px;
  }
  .band--pale { background: var(--green-pale); color: var(--green-ink); }
  .band--light { background: var(--green-light); color: var(--green-ink); }
  .band--mid { background: var(--green-mid); color: #fff; }
  .band--deep { background: var(--green-deep); color: #fff; }
  .clients-heading { left: 0; top: 23px; width: 301px; padding-left: 27px; font-size: 17px; }

  .testimonial {
    position: absolute; left: 15px; width: 272px; height: 86px;
    background: var(--card); border-radius: 10px;
    box-shadow: 0 2px 2px rgba(0,0,0,.15);
  }
  .portrait {
    position: absolute; border-radius: 50%;
    background: radial-gradient(circle at 50% 40%, var(--photo-b), var(--photo-a));
    border: 2px solid #fff;
  }
  .testimonial .portrait { left: 18px; top: 8px; width: 60px; height: 60px; }
  .testimonial p {
    position: absolute; left: 94px; top: 10px; width: 164px;
    font-size: 8.6px; line-height: 11.3px; color: #333;
  }
  .testimonial .client-name {
    position: absolute; left: 94px; top: 61px; font-size: 8.6px; font-weight: 800; color: var(--text-dark);
  }

  .chairman-heading {
    left: 0; top: 378px; width: 301px; text-align: center;
    font-size: 15.5px; font-weight: 800; color: var(--text-dark);
  }
  .chairman-box {
    left: 15px; top: 409px; width: 272px; height: 244px;
    background: var(--green-deep); border-radius: 10px; color: #fff;
    box-shadow: 0 2px 2px rgba(0,0,0,.15);
  }
  .chairman-box .portrait { left: 24px; top: 9px; width: 60px; height: 60px; }
  .chairman-name { left: 95px; top: 24px; font-size: 13px; font-weight: 800; }
  .chairman-sub { left: 95px; top: 41px; font-size: 8.6px; line-height: 11px; color: #dfe6c4; }
  .chairman-body {
    left: 11px; top: 76px; width: 244px; font-size: 8.6px; line-height: 11.2px;
    text-align: justify; color: #f4f6ea;
  }
  .chairman-body p + p { margin-top: 11px; }

  /* Middle panel */
  .contact-heading {
    left: 300px; top: 32px; width: 310px; text-align: center;
    font-size: 21px; font-weight: 800; color: var(--text-dark);
  }
  .photo { position: absolute; background: linear-gradient(135deg, var(--photo-a), var(--photo-b) 60%, #8aa267); }
  .photo--contact { left: 301px; top: 81px; width: 309px; height: 192px; border-top: 4px solid var(--green-mid); }
  .brand-mark { position: absolute; border-radius: 50%; background: var(--green-deep); border: 3px solid #fff; }
  .brand-mark--small { left: 344px; top: 234px; width: 62px; height: 62px; }
  .brand-name { position: absolute; color: var(--text-dark); font-weight: 400; letter-spacing: .5px; }
  .brand-name--small { left: 320px; top: 296px; font-size: 17px; }

  .intro-box {
    left: 320px; top: 322px; width: 270px; height: 148px;
    background: var(--green-pale); border-radius: 10px;
    padding: 14px 16px 0 20px; font-size: 11px; line-height: 13.4px;
    color: var(--green-ink); text-align: justify;
  }
  .address {
    left: 300px; top: 490px; width: 310px; text-align: center;
    font-size: 13.5px; line-height: 17px; color: var(--text-dark);
  }
  .address strong { font-size: 15px; font-weight: 800; display: block; margin-bottom: 1px; }
  .social { left: 300px; top: 601px; width: 310px; display: flex; justify-content: center; gap: 18px; }
  .social span { width: 29px; height: 29px; border-radius: 50%; background: var(--green-deep); display: block; }
  .social-handle { left: 300px; top: 638px; width: 310px; text-align: center; font-size: 11px; color: var(--text-dark); }

  /* Right panel */
  .service { left: 610px; width: 310px; justify-content: center; }
  .photo--services { left: 610px; top: 233px; width: 310px; height: 242px; border-bottom: 6px solid var(--green-deep); }
  .brand-mark--large { left: 713px; top: 463px; width: 106px; height: 106px; border: 4px solid var(--text-dark); }
  .brand-name--large { left: 610px; top: 558px; width: 310px; text-align: center; font-size: 30px; }
  .tagline { left: 610px; top: 627px; width: 310px; text-align: center; font-size: 11.5px; color: var(--text-dark); }
</style>
</head>
<body>
<div class="brochure">

  <!-- Left panel -->
  <div class="band band--pale clients-heading">What Our Clients Say...</div>

  <div class="testimonial" style="top:81px">
    <div class="portrait" role="img" aria-label="Portrait photo of a smiling senior couple"></div>
    <p>Lorem ipsum dolor sit amet, consectetuer adipiscing elit, sed diam nonummy nibh euismod tincidunt ut laoreet dolore magna aliquam erat volutpat.</p>
    <span class="client-name">Alfred &amp; Betty</span>
  </div>
  <div class="testimonial" style="top:178px">
    <div class="portrait" role="img" aria-label="Portrait photo of a man with glasses"></div>
    <p>Lorem ipsum dolor sit amet, consectetuer adipiscing elit, sed diam nonummy nibh euismod tincidunt ut laoreet dolore magna aliquam erat volutpat.</p>
    <span class="client-name">Donald</span>
  </div>
  <div class="testimonial" style="top:275px">
    <div class="portrait" role="img" aria-label="Portrait photo of a smiling woman"></div>
    <p>Lorem ipsum dolor sit amet, consectetuer adipiscing elit, sed diam nonummy nibh euismod tincidunt ut laoreet dolore magna aliquam erat volutpat.</p>
    <span class="client-name">Martha</span>
  </div>

  <h2 class="abs chairman-heading">Message from Our Chairman</h2>
  <div class="abs chairman-box">
    <div class="portrait" role="img" aria-label="Portrait photo of the chairman"></div>
    <div class="abs chairman-name">Dr. Doctor’s Name</div>
    <div class="abs chairman-sub">Lorem ipsum dolor sit amet<br>sed diam nonummy nibh euismod</div>
    <div class="abs chairman-body">
      <p>Lorem ipsum dolor sit amet, consectetuer adipiscing elit, sed diam nonummy nibh euismod tincidunt ut laoreet dolore magna aliquam erat volutpat. Ut wisi enim ad minim veniam, quis nostrud exerci tation ullamcorper suscipit lobortis nisl ut aliquip ex ea commodo consequat.</p>
      <p>Duis autem vel eum iriure dolor in hendrerit in vulputate velit esse molestie consequat, vel illum dolore eu feugiat nulla facilisis at vero eros et accumsan et iusto odio dignissim qui blandit praesent luptatum zzril delenit augue duis dolore te feugait nulla facilisi.</p>
    </div>
  </div>

  <!-- Middle panel -->
  <h2 class="abs contact-heading">Contact Us</h2>
  <div class="photo photo--contact" role="img" aria-label="Photo of a group of laughing seniors outdoors in a park"></div>
  <div class="brand-mark brand-mark--small"></div>
  <div class="brand-name brand-name--small">VELTIWEL</div>

  <div class="abs intro-box">Lorem ipsum dolor sit amet, consectetuer adipiscing elit, sed diam nonummy nibh euismod tincidunt ut laoreet dolore magna aliquam erat volutpat. Ut wisi enim ad minim veniam, quis nostrud exerci tation ullamcorper suscipit lobortis nisl ut aliquip ex ea commodo consequat.</div>

  <div class="abs address">
    <strong>Company Name in Full</strong>
    Address line 1,<br>
    Address line 2 line 2<br>
    Phone: 00 000 0000<br>
    Email: info@veltiwel.com
  </div>
  <div class="abs social"><span></span><span></span><span></span></div>
  <div class="abs social-handle">veltiwel</div>

  <!-- Right panel -->
  <div class="band band--pale service" style="top:23px">Chronic Care Management</div>
  <div class="band band--light service" style="top:76px">Physical Therapy</div>
  <div class="band band--mid service" style="top:129px">Rehabilitation</div>
  <div class="band band--deep service" style="top:182px">Medications Management</div>
  <div class="photo photo--services" role="img" aria-label="Photo of smiling seniors stacking hands together outdoors"></div>
  <div class="brand-mark brand-mark--large"></div>
  <div class="brand-name brand-name--large">VELTIWEL</div>
  <div class="abs tagline">Home and Community Based Services for Adults</div>

</div>
</body>
</html>
```